Fern and Slate Mobile Bartending Website

Looking for an informational website for our mobile bartending business. We want to include features we like from another website that will help support our business.

Something with a similar set-up to https://velvetfinchpours.com/

```html
<!DOCTYPE html>
<html lang="en">
<head>
<meta charset="utf-8">
<title>Fern &amp; Slate Mobile Bartending</title>
<link rel="stylesheet" href="https://fonts.googleapis.com/css2?family=Poppins:wght@600;700;800&family=Mulish:wght@300;400;500;600;700&display=swap">
<style>
:root{
  --pink:#f9c6c3;
  --blue:#b9ccdb;
  --ink:#111111;
  --text:#4a4a4a;
  --muted:#6b6b6b;
  --paper:#ffffff;
  --mist:#f5f3f2;
  --night:#161616;
  --star:#f5b50a;
}
*{box-sizing:border-box;margin:0;padding:0}
html,body{width:1200px;height:4107px;overflow:hidden}
body{font-family:"Mulish",sans-serif;color:var(--text);background:var(--paper);position:relative}
.heading{font-family:"Poppins",sans-serif;font-weight:700;color:var(--ink);text-transform:uppercase;text-align:center}
.btn{display:inline-block;font-family:"Mulish",sans-serif;font-weight:600;font-size:13px;color:var(--ink);background:var(--pink);text-transform:uppercase;text-decoration:none;letter-spacing:.2px}
.section{position:absolute;left:0;width:1200px}
.wrap{position:absolute;left:134px;width:934px}
.divider{display:flex;align-items:center;justify-content:center;gap:14px}
.divider span{display:block;height:1px;background:var(--ink)}
.divider i{display:block;width:40px;height:40px;background:var(--ink)}
.brand{font-family:"Mulish",sans-serif;font-weight:600;color:var(--ink);display:flex;align-items:center;gap:8px;text-transform:uppercase}
.brand b{display:block;background:currentColor}

/* header */
.site-header{top:0;height:91px;background:var(--paper)}
.site-header .brand{position:absolute;left:136px;top:32px;font-size:18px}
.site-header .brand b{width:14px;height:14px}
.main-nav{position:absolute;right:132px;top:26px;display:flex;align-items:center;gap:38px}
.main-nav a{font-size:13px;font-weight:600;color:var(--ink);text-decoration:none;text-transform:uppercase}
.main-nav .btn{padding:10px 15px}

/* hero */
.hero{top:91px;height:572px;background:linear-gradient(100deg,#6b4a3a 0%,#8c5a40 30%,#a88a6e 52%,#d9d4cf 68%,#b0203a 85%,#7d1a27 100%)}
.hero-photo{position:absolute;inset:0}
.hero-copy{position:absolute;left:133px;top:115px;width:430px}
.hero-copy h1{font-family:"Poppins",sans-serif;font-weight:700;font-size:43px;line-height:57px;color:#fff;text-transform:uppercase}
.hero-copy p{margin-top:22px;font-size:17px;line-height:24px;color:#fff}
.hero-copy .btn{margin-top:28px;padding:14px 22px}
.hero-dots{position:absolute;left:144px;top:484px;display:flex;gap:12px}
.hero-dots i{width:12px;height:12px;border-radius:50%;background:#fff}
.hero-dots i:first-child{background:var(--pink)}

/* welcome */
.welcome{top:663px;height:400px;background:var(--paper)}
.welcome .divider{position:absolute;left:0;width:1200px;top:40px}
.welcome .divider span{width:133px}
.welcome h2{position:absolute;top:110px;width:1200px;font-size:26px}
.welcome p{position:absolute;left:205px;width:790px;top:168px;text-align:center;font-size:13.5px;line-height:22.5px}
.welcome .btn{position:absolute;left:536px;top:304px;padding:15px 22px}

/* services */
.services{top:1063px;height:574px;background:var(--mist)}
.services .divider{position:absolute;left:0;width:1200px;top:35px}
.services .divider span{width:115px}
.services h2{position:absolute;top:104px;width:1200px;font-size:26px}
.service-grid{position:absolute;left:134px;top:168px;width:934px;display:grid;grid-template-columns:295px 295px 295px;column-gap:24px}
.service-card .photo{height:294px}
.service-card .label{height:66px;background:var(--blue);display:flex;align-items:center;justify-content:center;font-size:17px;font-weight:500;color:var(--ink);text-transform:uppercase}
.photo-bar{background:linear-gradient(160deg,#f3c04a 0%,#a8611c 45%,#2d1608 100%)}
.photo-cocktails{background:linear-gradient(170deg,#1e1b18 0%,#5a8a5a 35%,#d0462e 60%,#5c3a20 100%)}
.photo-whiskey{background:linear-gradient(165deg,#2c2b28 0%,#4d4a44 40%,#c67a26 65%,#2a2825 100%)}

/* testimonials */
.testimonials{top:1637px;height:495px;background:var(--paper)}
.testimonials .divider{position:absolute;left:0;width:1200px;top:40px}
.testimonials .divider span{width:62px}
.testimonials h2{position:absolute;top:109px;width:1200px;font-size:26px}
.quote-card{position:absolute;top:176px;width:451px;height:267px;background:var(--paper);box-shadow:0 4px 20px rgba(0,0,0,.08);padding:22px 36px 0 65px}
.quote-card .mark{position:absolute;left:32px;top:18px;font-family:"Poppins",sans-serif;font-size:44px;line-height:1;color:var(--pink)}
.quote-card p{margin-top:20px;font-size:13.5px;line-height:22.5px}
.reviewer{display:flex;align-items:center;gap:12px;margin-top:18px;margin-left:-10px}
.reviewer .avatar{width:42px;height:42px;border-radius:50%;background:linear-gradient(135deg,#6e8aa6,#c9b49b)}
.reviewer strong{display:block;font-size:14px;font-weight:600;color:var(--ink)}
.reviewer svg{display:block;margin-top:4px}
.slider-arrow{position:absolute;top:296px}

/* request banner */
.request{top:2132px;height:434px;background:linear-gradient(110deg,#2e2c28 0%,#4b4740 35%,#3a3632 60%,#22201d 100%)}
.request h2{position:absolute;top:110px;left:0;width:1212px;font-family:"Poppins",sans-serif;font-weight:800;font-size:39px;line-height:48px;color:#fff;text-transform:uppercase;text-align:center}
.request .btn{position:absolute;left:487px;top:238px;padding:15px 22px}

/* event cards */
.events{top:2566px;height:414px;background:var(--paper)}
.event-card{position:absolute;top:48px;width:451px;height:310px;text-align:center;padding-top:38px}
.event-card.blue{left:134px;background:var(--blue)}
.event-card.pink{left:617px;background:var(--pink)}
.event-card h3{margin-top:28px;font-family:"Poppins",sans-serif;font-weight:700;font-size:23px;color:var(--ink);text-transform:uppercase}
.event-card p{margin:14px auto 0;width:370px;font-size:13.5px;line-height:22px}
.event-card .btn{margin-top:20px;background:var(--paper);padding:13px 22px;font-size:13px}

/* contact */
.contact{top:2980px;height:711px;background:var(--mist)}
.contact .divider{position:absolute;left:0;width:1200px;top:40px}
.contact .divider span{width:105px}
.contact h2{position:absolute;top:108px;width:1200px;font-size:26px}
.info-box{position:absolute;top:180px;width:295px;height:158px;background:var(--paper);display:flex;flex-direction:column;align-items:center;justify-content:center;text-align:center;font-size:17px;line-height:29px;color:#222}
.info-box small{font-size:16px;color:var(--muted);text-transform:uppercase;font-weight:400}
.info-box .email{font-size:14px}
.contact h3{position:absolute;top:382px;width:1200px;font-family:"Poppins",sans-serif;font-weight:700;font-size:18px;color:var(--ink);text-align:center;text-transform:uppercase}
.contact .lead{position:absolute;top:417px;width:1200px;text-align:center;font-size:13.5px}
.field{position:absolute;width:340px;height:44px;background:var(--blue);color:#fff;font-size:14px;font-weight:600;padding:13px 20px}
.submit{position:absolute;left:540px;top:601px;width:120px;height:44px;background:var(--pink);font-family:"Mulish",sans-serif;font-size:19px;font-weight:500;color:var(--ink);text-align:center;line-height:44px}

/* gallery */
.gallery{top:3691px;height:232px;background:var(--paper)}
.gallery .shot{position:absolute;top:0;width:226px;height:216px}
.shot-1{left:11px;background:linear-gradient(150deg,#3b7a8e,#c49a74,#4a3a2c)}
.shot-2{left:250px;background:linear-gradient(150deg,#f0c16a,#a2705a,#3d3a2c)}
.shot-3{left:489px;background:linear-gradient(160deg,#24313d,#43576a,#1c232b)}
.shot-4{left:728px;background:linear-gradient(150deg,#efece6,#c9b79c,#9b8466)}
.shot-5{left:964px;background:linear-gradient(160deg,#a2a7aa,#e2d02c,#59584f)}
.gallery .arrow{position:absolute;top:84px}

/* footer */
.site-footer{top:3923px;height:184px;background:var(--night);color:#fff}
.site-footer .brand{position:absolute;left:140px;top:84px;font-size:29px;color:#fff;font-weight:500}
.site-footer .brand b{width:18px;height:18px}
.follow{position:absolute;right:132px;top:38px;display:flex;align-items:center;gap:8px;font-size:13px;font-weight:700}
.follow i{display:block;width:22px;height:22px;border-radius:4px;background:#fff}
.follow span{margin-right:8px}
.footer-nav{position:absolute;right:132px;top:86px;display:flex;gap:36px}
.footer-nav a{color:#fff;text-decoration:none;font-size:13px;font-weight:700;text-transform:uppercase}
.copyright{position:absolute;right:132px;top:133px;font-size:12px}
</style>
</head>
<body>

<header class="section site-header">
  <div class="brand"><b></b>Fern &amp; Slate</div>
  <nav class="main-nav">
    <a href="#">Packages + Bars</a>
    <a href="#">Cocktail Menu</a>
    <a href="#">Request Our Services</a>
    <a href="#" class="btn">Schedule Consult</a>
  </nav>
</header>

<section class="section hero">
  <div class="hero-photo" role="img" aria-label="Couple holding glasses of red wine in front of a vintage mobile bar trailer"></div>
  <div class="hero-copy">
    <h1>Fern &amp; Slate Mobile Bartending</h1>
    <p>Lorem ipsum dolor sit amet, consectetur adip iscing elit, sed do eiusmod tempor incididunt ut labore et dolore magna aliqua.</p>
    <a href="#" class="btn">View Our Packages</a>
  </div>
  <div class="hero-dots"><i></i><i></i><i></i></div>
</section>

<section class="section welcome">
  <div class="divider"><span></span><i></i><span></span></div>
  <h2 class="heading">Welcome to Fern &amp; Slate</h2>
  <p>Sed ut perspiciatis unde omnis iste natus error sit voluptatem accusantium doloremque laudantium, totam rem aperiam, eaque ipsa quae ab illo inventore veritatis et quasi architecto beatae vitae dicta sunt explicabo. Nemo enim ipsam voluptatem quia voluptas sit aspernatur aut odit aut fugit, sed quia consequuntur magni dolores eos qui ratione volup tatem sequi nesciunt. Neque porro quisquam est, qui dolorem ipsum quia dolor sit amet, consectetur, adipisci velit, sed quia non numquam eius modi tempora incidunt ut labore et dolore magnam aliquam quaerat</p>
  <a href="#" class="btn">Read More</a>
</section>

<section class="section services">
  <div class="divider"><span></span><i></i><span></span></div>
  <h2 class="heading">Bartending Services</h2>
  <div class="service-grid">
    <div class="service-card"><div class="photo photo-bar" role="img" aria-label="Colorful cocktails on a warmly lit bar"></div><div class="label">Packages + Bars</div></div>
    <div class="service-card"><div class="photo photo-cocktails" role="img" aria-label="Row of mixed cocktails with fruit garnish"></div><div class="label">Cocktail Menu</div></div>
    <div class="service-card"><div class="photo photo-whiskey" role="img" aria-label="Glass of whiskey on ice on a dark table"></div><div class="label">Alcohol Calculator</div></div>
  </div>
</section>

<section class="section testimonials">
  <div class="divider"><span></span><i></i><span></span></div>
  <h2 class="heading">Testimonials</h2>
  <svg class="slider-arrow" style="left:66px" width="20" height="32" viewBox="0 0 20 32"><path d="M16 3 L4 16 L16 29" fill="none" stroke="#9a9a9a" stroke-width="2.5"/></svg>
  <article class="quote-card" style="left:134px">
    <span class="mark">&ldquo;</span>
    <p>Sed ut perspiciatis unde omnis iste natus error sit volup tatem accusantium doloremque laudantium, totam rem aperiam, eaque ipsa quae ab illo inventore veritatis et quasi architecto beatae vitae dicta sunt explicabo. Nemo enim ipsam voluptatem quia voluptas sit aspernatur aut odit aut fugit</p>
    <div class="reviewer"><div class="avatar" role="img" aria-label="Reviewer portrait"></div><div><strong>Daniel</strong>
      <svg width="70" height="12" viewBox="0 0 70 12"><g fill="#f5b50a"><path id="st" d="M6 0l1.8 3.9 4.2.4-3.2 2.8 1 4.1L6 9 2.2 11.2l1-4.1L0 4.3l4.2-.4z"/><use href="#st" x="14"/><use href="#st" x="28"/><use href="#st" x="42"/><use href="#st" x="56"/></g></svg></div></div>
  </article>
  <article class="quote-card" style="left:617px">
    <span class="mark">&ldquo;</span>
    <p>Sed ut perspiciatis unde omnis iste natus error sit volup tatem accusantium doloremque laudantium, totam rem aperiam, eaque ipsa quae ab illo inventore veritatis et quasi architecto beatae vitae dicta sunt explicabo. Nemo enim ipsam voluptatem quia voluptas sit aspernatur aut odit aut fugit</p>
    <div class="reviewer"><div class="avatar" role="img" aria-label="Reviewer portrait"></div><div><strong>Daniel</strong>
      <svg width="70" height="12" viewBox="0 0 70 12"><g fill="#f5b50a"><use href="#st"/><use href="#st" x="14"/><use href="#st" x="28"/><use href="#st" x="42"/><use href="#st" x="56"/></g></svg></div></div>
  </article>
  <svg class="slider-arrow" style="left:1108px" width="20" height="32" viewBox="0 0 20 32"><path d="M4 3 L16 16 L4 29" fill="none" stroke="#9a9a9a" stroke-width="2.5"/></svg>
</section>

<section class="section request" role="img" aria-label="Guests ordering drinks at a dark food truck bar strung with bunting">
  <h2>Request our services<br>for your next event!</h2>
  <a href="#" class="btn">Schedule Consultation</a>
</section>

<section class="section events">
  <div class="event-card blue">
    <svg width="106" height="62" viewBox="0 0 106 62"><g fill="none" stroke="#111" stroke-width="4"><rect x="4" y="4" width="66" height="40"/><path d="M70 16h18l14 16v12H70z"/><circle cx="24" cy="50" r="8" fill="#b9ccdb"/><circle cx="84" cy="50" r="8" fill="#b9ccdb"/></g><rect x="12" y="12" width="50" height="10" fill="#111"/></svg>
    <h3>Package + Bars</h3>
    <p>Sed ut perspiciatis unde omnis iste natus error sit volup tatem accusantium doloremque laudantium.</p>
    <a href="#" class="btn">Schedule Consultation</a>
  </div>
  <div class="event-card pink">
    <svg width="106" height="62" viewBox="0 0 106 62"><g fill="none" stroke="#111" stroke-width="4"><rect x="4" y="4" width="66" height="40"/><path d="M70 16h18l14 16v12H70z"/><circle cx="24" cy="50" r="8" fill="#f9c6c3"/><circle cx="84" cy="50" r="8" fill="#f9c6c3"/></g><rect x="12" y="12" width="50" height="10" fill="#111"/></svg>
    <h3>Tell us about your event</h3>
    <p>Sed ut perspiciatis unde omnis iste natus error sit volup tatem accusantium doloremque laudantium.</p>
    <a href="#" class="btn">Schedule Consultation</a>
  </div>
</section>

<section class="section contact">
  <div class="divider"><span></span><i></i><span></span></div>
  <h2 class="heading">Contact Fern &amp; Slate</h2>
  <div class="info-box" style="left:134px"><small>Phone Number</small>+1 888 888 8888</div>
  <div class="info-box" style="left:454px"><small>Our Address</small>2170 Linden Row<br>Alder Falls, MN 55990</div>
  <div class="info-box" style="left:774px"><small>Email Address</small><span class="email">info@fernslatemobilebartending.com</span></div>
  <h3>Let&rsquo;s Stay Connected</h3>
  <p class="lead">Sed ut perspiciatis unde omnis iste natus error sit volup tatem accusantium doloremque laudantium</p>
  <div class="field" style="left:250px;top:466px">First Name</div>
  <div class="field" style="left:609px;top:466px">Last Name</div>
  <div class="field" style="left:250px;top:526px">Email id</div>
  <div class="field" style="left:609px;top:526px">Phone</div>
  <div class="submit">SUBMIT</div>
</section>

<section class="section gallery">
  <div class="shot shot-1" role="img" aria-label="Bartender serving a guest from a mobile bar"></div>
  <div class="shot shot-2" role="img" aria-label="Guests gathered at an outdoor event at sunset"></div>
  <div class="shot shot-3" role="img" aria-label="Dark mobile bar trailer"></div>
  <div class="shot shot-4" role="img" aria-label="Hand reaching for a glass on a bright counter"></div>
  <div class="shot shot-5" role="img" aria-label="Yellow food truck parked on a street"></div>
  <svg class="arrow" style="left:44px" width="20" height="34" viewBox="0 0 20 34"><path d="M16 3 L4 17 L16 31" fill="none" stroke="#fff" stroke-width="3"/></svg>
  <svg class="arrow" style="left:1136px" width="20" height="34" viewBox="0 0 20 34"><path d="M4 3 L16 17 L4 31" fill="none" stroke="#fff" stroke-width="3"/></svg>
</section>

<footer class="section site-footer">
  <div class="brand"><b></b>Fern &amp; Slate</div>
  <div class="follow"><span>FOLLOW US</span><i></i><i></i></div>
  <nav class="footer-nav">
    <a href="#">Packages + Bars</a>
    <a href="#">Cocktail Menu</a>
    <a href="#">Request Our Services</a>
  </nav>
  <div class="copyright">Copyright &copy; 2023 All Rights Reserved</div>
</footer>

</body>
</html>
```